Meadowlyn Acres Website Design

We have been redeveloping our website already and are quite happy with the content, but the design needs to be better:
https://harvo-link.example-host.com/

Pages, content, concept etc. Can all be taken from the redeveloped website.
The farmer can register and edit/view their profile, subscribe and these pages need to be designed better as well as contact, about, pricing, tos, privacy and a page with example portlets.

We need a website to appeal to farmers, investors and retiring farmers.

The design should be clean and a little country.

We don't want any repeat designs that some may submit to every project and has no respect for the project brief, so please don't submit them.

Target Market(s)

farmers, investors, retirees

Industry/Entity Type

Farming

Number of Pages Required

5+ page

Colors

Designer to choose colors to be used in the design.

Requirements
Must have
• Nice, clean modern design that is appealing
• Profile page laid out nicely

```html
<!DOCTYPE html>
<html lang="en">
<head>
<meta charset="utf-8">
<title>Meadowlyn Acres – Farmer Profile</title>
<link href="https://fonts.googleapis.com/css2?family=Roboto:wght@300;400;700&display=swap" rel="stylesheet">
<style>
:root{
  --green:#38a335;
  --green-dark:#2e8a2c;
  --ink:#2b2b2b;
  --muted:#8a8a8a;
  --line:#c9c9c9;
  --red:#e0201d;
  --paper:#ffffff;
}
*{box-sizing:border-box;margin:0;padding:0}
html,body{width:1200px;height:655px;overflow:hidden;background:var(--paper)}
body{position:relative;font-family:"Roboto",Arial,sans-serif;font-weight:300;color:var(--ink)}
.screen{position:absolute;top:0;height:655px;background:var(--paper);overflow:hidden}
.screen--edit{left:0;width:570px}
.screen--view{left:589px;width:611px}
.abs{position:absolute;white-space:nowrap;line-height:1}
.hero{position:absolute;left:0;top:0;width:100%;
  background:linear-gradient(180deg,#8da1ac 0%,#aeb9bd 42%,#6f6446 60%,#a88650 78%,#c7a46a 100%)}
.screen--edit .hero{height:166px}
.screen--view .hero{height:178px}
.dot{display:inline-block;width:9px;height:9px;border-radius:50%;background:var(--green);margin-right:4px;vertical-align:middle}
.pill{position:absolute;border:1px solid var(--green);border-radius:10px;color:var(--green);font-size:8.5px;font-weight:400;display:flex;align-items:center;justify-content:center}
.pill--solid{background:var(--green);color:#fff}
.brand{position:absolute;display:flex;align-items:center;gap:8px;color:var(--ink);font-weight:400}
.brand .mark{width:18px;height:18px;border-radius:50%;border:1.5px solid var(--green)}
.nav{position:absolute;font-size:8px;font-weight:400;color:#222;display:flex}
.photo-frame{position:absolute;border:4px solid var(--green);background:linear-gradient(160deg,#7b6a58,#b49b80 55%,#d8d2c6)}
.edit-tag{position:absolute;color:#fff;font-size:8px;font-weight:400}
.name{color:var(--green);font-weight:700;letter-spacing:.3px}
.since{color:var(--muted);font-size:7.5px}
.role{color:var(--green);font-weight:700}
.link-u{color:var(--muted);text-decoration:underline;font-weight:300}
.h-sec{color:var(--green);font-weight:700;font-size:10px;letter-spacing:.2px}
.info{position:absolute;font-size:8px;line-height:13.5px}
.info b{font-weight:400;color:var(--ink)}
.info span{color:var(--muted)}
.social{position:absolute;font-size:7.2px;color:var(--muted);line-height:13.8px}
.social .dot{width:7px;height:7px;margin-right:9px}
.gallery{position:absolute;border:1px solid var(--line)}
.gallery .g-title{position:absolute;color:var(--green);font-weight:700;font-size:10px}
.grid{position:absolute;display:grid}
.grid div{background:#8a7a55}
.q{position:absolute;width:330px}
.q h3{color:var(--green);font-weight:700;font-size:10px;margin-bottom:5px}
.q p{color:var(--muted);font-size:7.8px;line-height:11.5px}
.q .ed{color:var(--muted);font-weight:300;text-decoration:underline;font-size:9px;margin-left:4px}
.lab{position:absolute;font-size:8px;font-weight:400;text-align:right}
.box{position:absolute;border:1px solid var(--line);font-size:7.4px;color:var(--muted);line-height:10.5px;overflow:hidden}
.box .ph{border-bottom:1px solid var(--line);font-size:6px;color:#bbb;padding:1px 4px;line-height:9px}
.box .vals{padding:1px 2px;white-space:nowrap}
.check{display:inline-block;width:8px;height:8px;border:1px solid #999;vertical-align:-1px;margin-right:3px;font-size:7px;line-height:6px;text-align:center;color:#333}
.val{position:absolute;font-size:8px;color:var(--muted);line-height:10.3px}
.foot{position:absolute;font-size:9px;color:#333;font-weight:300;display:flex;align-items:center}
.foot .sup{color:var(--green);font-weight:700;margin-right:3px}
.foot .sep{margin:0 6px}
</style>
</head>
<body>

<!-- Edit profile screen -->
<section class="screen screen--edit">
  <div class="hero" role="img" aria-label="Wide rural landscape of golden pasture with trees and grazing cattle under a pale sky"></div>
  <div class="abs" style="left:248px;top:16px"><span class="dot"></span><span class="dot"></span><span class="dot"></span></div>
  <div class="pill pill--solid" style="left:286px;top:13px;width:40px;height:15px">Donate</div>
  <div class="brand" style="left:16px;top:38px;font-size:14px"><span class="mark"></span>Meadowlyn Acres</div>
  <nav class="nav" style="left:177px;top:44px;gap:12px"><span>Home</span><span>Aspiring Farmers</span><span>Farming Investors</span><span>Retiring Farmers</span><span>Our Blog</span><span>Pricing</span></nav>
  <div class="pill" style="left:513px;top:40px;width:40px;height:16px">Log out</div>
  <div class="edit-tag" style="left:546px;top:151px;text-decoration:underline">Edit</div>

  <div class="photo-frame" style="left:231px;top:108px;width:108px;height:107px" role="img" aria-label="Profile photo of the farmer cooking in a kitchen"></div>
  <div class="edit-tag" style="left:316px;top:200px;text-decoration:underline">Edit</div>

  <div class="abs name" style="left:352px;top:177px;font-size:18.5px">CALLUM BRENNAN</div>
  <div class="abs since" style="left:352px;top:198px">Memerber since April, 2017</div>
  <div class="abs role" style="left:352px;top:208px;font-size:10px">Aspiring Farmer <span class="link-u" style="margin-left:4px">View Packages</span></div>

  <div class="abs h-sec" style="left:51px;top:181px">GENERAL INFORMATION <span class="link-u" style="font-size:8.5px;margin-left:3px">Edit</span></div>
  <div class="info" style="left:51px;top:199px">
    <div><b>Email:</b> <span>brennan.callum@mailbox.example</span></div>
    <div><b>Phone:</b> <span>0300 118 472</span></div>
    <div><b>State:</b> <span>Victoria</span></div>
    <div><b>Closest town:</b> <span>bendigo</span></div>
    <div style="line-height:10px;margin-top:2px"><b>Interested areas:</b> <span>Canberra,</span><br><span>South-Est Queensland</span></div>
    <div style="margin-top:2px"><b>Current Job:</b> <span>Manager</span></div>
    <div><b>Status:</b> <span>Married with kids</span></div>
  </div>

  <div class="abs h-sec" style="left:50px;top:317px">SOCIAL MEDIA LINKS <span class="link-u" style="font-size:8.5px;margin-left:3px">Edit</span></div>
  <div class="social" style="left:51px;top:332px">
    <div><span class="dot"></span>http://cbrennan.work-network.example</div>
    <div><span class="dot"></span>http://brennanc.shortposts.example</div>
    <div><span class="dot"></span>http://callumbrennan.friendpage.example</div>
    <div><span class="dot"></span>http://cattlelover.photoshare.example</div>
  </div>

  <div class="gallery" style="left:44px;top:403px;width:156px;height:170px">
    <div class="g-title" style="left:5px;top:4px">CALLUM'S GALLERY</div>
    <div class="link-u abs" style="left:136px;top:6px;font-size:8.5px">Edit</div>
    <div class="grid" style="left:4px;top:18px;grid-template-columns:repeat(3,47px);grid-auto-rows:47px;gap:3px">
      <div role="img" aria-label="Farm shed interior" style="background:#7a5a3e"></div>
      <div role="img" aria-label="Hay bales in a paddock" style="background:#8f8a5a"></div>
      <div role="img" aria-label="Family outdoors" style="background:#b0886e"></div>
      <div role="img" aria-label="Paddock with trees" style="background:#6f7e52"></div>
      <div role="img" aria-label="Orchard rows" style="background:#5e7a46"></div>
      <div role="img" aria-label="Cattle on open pasture" style="background:#8c7a55"></div>
      <div role="img" aria-label="Horse riding in a field" style="background:#7e8a66"></div>
      <div role="img" aria-label="Cattle grazing" style="background:#7d6f4e"></div>
      <div role="img" aria-label="Family group portrait" style="background:#6a7a5c"></div>
    </div>
  </div>

  <div class="abs h-sec" style="left:228px;top:230px">BACKGROUND AND EXPERIENCE <span style="color:var(--red);text-decoration:underline;font-weight:400;font-size:9px;margin-left:3px">Save changes</span></div>

  <div class="lab" style="left:200px;top:250px;width:111px">Years of experience:</div>
  <div class="box" style="left:316px;top:248px;width:57px;height:12px;padding:1px 2px;font-size:7.5px;line-height:9px">0-1 years<span style="position:absolute;right:0;top:0;width:12px;height:10px;background:#ddd"></span></div>

  <div class="lab" style="left:200px;top:265px;width:111px">Preferences:</div>
  <div class="box" style="left:316px;top:263px;width:231px;height:48px">
    <div class="ph">Start typing and select from the list...</div>
    <div class="vals">Beef, Other livestock, Sheep, Market garden,<br>Chickens, Specialty Crops, Dairy, Broad Acre<br>Cropping, Goats, Viticulture</div>
  </div>

  <div class="lab" style="left:200px;top:317px;width:111px">Farming Skills:</div>
  <div class="box" style="left:316px;top:315px;width:231px;height:58px">
    <div class="ph">Start typing and select from the list...</div>
    <div class="vals">Cropping, Business Management, Livestock<br>Mustering, Human Resources, Marketing, Sales,<br>Book Keeping, Machinery Operation, Planning, Fencing,<br>Accounting, Agronomy, Animal Husbandry</div>
  </div>

  <div class="lab" style="left:200px;top:377px;width:111px">Farming Methods:</div>
  <div class="box" style="left:316px;top:376px;width:231px;height:37px">
    <div class="ph">Start typing and select from the list...</div>
    <div class="vals">Grass fed, Biodynamic, Conventional, Organic,<br>Regenerative, Permaculture</div>
  </div>

  <div class="lab" style="left:200px;top:418px;width:111px">Farming Options:</div>
  <div class="abs" style="left:319px;top:419px;font-size:6px;color:#bbb">Select all that apply:</div>
  <div class="abs" style="left:316px;top:429px;font-size:7.5px;color:var(--muted)">
    <span class="check">x</span>Lease <span class="check" style="margin-left:6px">x</span>Share Farm <span class="check" style="margin-left:6px"></span>Own <span class="check" style="margin-left:6px"></span>Rent
  </div>

  <div class="q" style="left:228px;top:449px">
    <h3>What have you been doing to get farm ready?<span class="ed">Edit</span></h3>
    <p>Everything! Got my liscences to drive tractors and other farming machinery,<br>got as much experience helping out at a XYZ farms.</p>
  </div>
  <div class="q" style="left:228px;top:494px">
    <h3>Why are you persuing farming?<span class="ed">Edit</span></h3>
    <p>I really love to farm as farming is forever. I would love to farm anywhere<br>there is an opportunity to live and work in a local farming community.</p>
  </div>
  <div class="q" style="left:228px;top:538px">
    <h3>How do you envision your dream farm to be like?<span class="ed">Edit</span></h3>
    <p>I really love to farm as farming is forever. I would love to farm anywhere<br>there is an opportunity to live and work in a local farming community.</p>
  </div>

  <div class="foot" style="left:13px;top:626px">© Meadowlyn Acres 2017</div>
  <div class="foot" style="left:195px;top:626px"><span class="sup">Support:</span>Contact<span class="sep">|</span>Terms of Service<span class="sep">|</span>Privacy<span class="sep">|</span>Newsletter</div>
  <div class="abs" style="left:473px;top:626px"><span class="dot"></span><span class="dot"></span><span class="dot"></span></div>
  <div class="pill" style="left:517px;top:622px;width:41px;height:16px">Donate</div>
</section>

<!-- Public profile screen -->
<section class="screen screen--view">
  <div class="hero" role="img" aria-label="Wide rural landscape of golden pasture with trees and grazing cattle under a pale sky"></div>
  <div class="abs" style="left:259px;top:17px"><span class="dot"></span><span class="dot"></span><span class="dot"></span></div>
  <div class="pill pill--solid" style="left:307px;top:14px;width:43px;height:16px;font-size:9px">Donate</div>
  <div class="brand" style="left:18px;top:40px;font-size:15px"><span class="mark" style="width:20px;height:20px"></span>Meadowlyn Acres</div>
  <nav class="nav" style="left:190px;top:47px;gap:14px;font-size:8.5px"><span>Home</span><span>Aspiring Farmers</span><span>Farming Investors</span><span>Retiring Farmers</span><span>Our Blog</span><span>Pricing</span></nav>
  <div class="pill" style="left:549px;top:42px;width:49px;height:18px;font-size:9px">Login</div>

  <div class="photo-frame" style="left:248px;top:117px;width:115px;height:114px" role="img" aria-label="Profile photo of the farmer cooking in a kitchen"></div>

  <div class="abs name" style="left:377px;top:190px;font-size:20px">CALLUM BRENNAN</div>
  <div class="abs since" style="left:377px;top:212px;font-size:8px">Member since April, 2017</div>
  <div class="abs role" style="left:377px;top:223px;font-size:10.5px">Aspiring Farmer</div>

  <div class="abs h-sec" style="left:55px;top:194px;font-size:10.5px">GENERAL INFORMATION</div>
  <div class="info" style="left:55px;top:212px;font-size:8.5px;line-height:14.6px">
    <div><b>Email:</b> <span>brennan.callum@mailbox.example</span></div>
    <div><b>Phone:</b> <span>0300 118 472</span></div>
    <div><b>State:</b> <span>Victoria</span></div>
    <div><b>Closest town:</b> <span>bendigo</span></div>
    <div style="line-height:10.5px;margin-top:2px"><b>Interested areas:</b> <span>Canberra,</span><br><span>South-Est Queensland</span></div>
    <div style="margin-top:2px"><b>Current Job:</b> <span>Manager</span></div>
    <div><b>Status:</b> <span>Married with kids</span></div>
  </div>

  <div class="abs h-sec" style="left:54px;top:340px;font-size:10.5px">SOCIAL MEDIA LINKS</div>
  <div class="social" style="left:55px;top:356px;font-size:7.8px;line-height:14.6px">
    <div><span class="dot"></span>http://cbrennan.work-network.example</div>
    <div><span class="dot"></span>http://brennanc.shortposts.example</div>
    <div><span class="dot"></span>http://callumbrennan.friendpage.example</div>
    <div><span class="dot"></span>http://cattlelover.photoshare.example</div>
  </div>

  <div class="gallery" style="left:45px;top:432px;width:169px;height:181px">
    <div class="g-title" style="left:8px;top:4px;font-size:10.5px">CALLUM'S GALLERY</div>
    <div class="grid" style="left:6px;top:18px;grid-template-columns:repeat(3,50px);grid-auto-rows:50px;gap:4px 4px">
      <div role="img" aria-label="Farm shed interior" style="background:#7a5a3e"></div>
      <div role="img" aria-label="Hay bales in a paddock" style="background:#8f8a5a"></div>
      <div role="img" aria-label="Family outdoors" style="background:#b0886e"></div>
      <div role="img" aria-label="Paddock with trees" style="background:#6f7e52"></div>
      <div role="img" aria-label="Orchard rows" style="background:#5e7a46"></div>
      <div role="img" aria-label="Cattle on open pasture" style="background:#8c7a55"></div>
      <div role="img" aria-label="Horse riding in a field" style="background:#7e8a66"></div>
      <div role="img" aria-label="Cattle grazing" style="background:#7d6f4e"></div>
      <div role="img" aria-label="Family group portrait" style="background:#6a7a5c"></div>
    </div>
  </div>

  <div class="abs h-sec" style="left:244px;top:247px;font-size:11px">BACKGROUND AND EXPERIENCE</div>

  <div class="lab" style="left:244px;top:268px;width:89px;font-size:8.5px">Years of experience:</div>
  <div class="val" style="left:339px;top:268px">0-1 years</div>
  <div class="lab" style="left:244px;top:283px;width:89px;font-size:8.5px">Preferences:</div>
  <div class="val" style="left:339px;top:284px">Beef, Other livestock, Sheep, Market garden, Chickens,<br>Specialty Crops, Dairy, Broad Acre Cropping, Goats,<br>Viticulture</div>
  <div class="lab" style="left:244px;top:323px;width:89px;font-size:8.5px">Farming Skills:</div>
  <div class="val" style="left:339px;top:323px">Cropping, Business Management, Livestock Mustering,<br>Human Resources, Marketing, Sales, Book Keeping,<br>Machinery, Operation, Planning, Fencing, Accounting,<br>Agronomy, Animal Husbandry</div>
  <div class="lab" style="left:244px;top:370px;width:89px;font-size:8.5px">Farming Methods:</div>
  <div class="val" style="left:339px;top:370px">Grass fed, Biodynamic, Conventional, Organic, Regenerative,<br>Permaculture</div>
  <div class="lab" style="left:244px;top:399px;width:89px;font-size:8.5px">Farming Options:</div>
  <div class="val" style="left:339px;top:399px">Lease, Share Farm</div>

  <div class="q" style="left:244px;top:426px;width:360px">
    <h3 style="font-size:10.5px">What have you been doing to get farm ready?</h3>
    <p style="font-size:8.2px;line-height:12px">Everything! Got my liscences to drive tractors and other farming machinery,<br>got as much experience helping out at a XYZ farms.</p>
  </div>
  <div class="q" style="left:244px;top:474px;width:360px">
    <h3 style="font-size:10.5px">Why are you persuing farming?</h3>
    <p style="font-size:8.2px;line-height:12px">I really love to farm as farming is forever. I would love to farm anywhere<br>there is an opportunity to live and work in a local farming community.</p>
  </div>
  <div class="q" style="left:244px;top:521px;width:360px">
    <h3 style="font-size:10.5px">How do you envision your dream farm to be like?</h3>
    <p style="font-size:8.2px;line-height:12px">I really love to farm as farming is forever. I would love to farm anywhere<br>there is an opportunity to live and work in a local farming community.</p>
  </div>

  <div class="foot" style="left:14px;top:630px;font-size:9.5px">© Meadowlyn Acres 2017</div>
  <div class="foot" style="left:209px;top:629px;font-size:9.5px"><span class="sup">Support:</span>Contact<span class="sep">|</span>Terms of Service<span class="sep">|</span>Privacy<span class="sep">|</span>Newsletter</div>
  <div class="abs" style="left:506px;top:630px"><span class="dot"></span><span class="dot"></span><span class="dot"></span></div>
  <div class="pill" style="left:554px;top:626px;width:44px;height:17px;font-size:9px">Donate</div>
</section>

</body>
</html>
```